HTML Digital Sign layout and code (one page)...save us from the 60's!

Digital Sign for Headquarters Entrance

HTML Digital Sign layout (one page)...save us from the 60's!

Good Day Designers!

We have decided to install Digital Signage in our headquarters building that will replace the “felt boards” that the administrative staff use at our building entrances.

Instead of the information being displayed on the archaic sign boards, it will be presented on a landscaped 50inch LCD screen running at 1920x1080

We are looking for a one page HTML design that encompass the following elements:

+ Our Logo
+ Our Company Name (Vorlan Aerotek)
+ Our "Tag Line" - "Progress Shaped By Practice, Quality Shaped By Dedication"
+ Date and Time
+ A space for Today’s Birthdays (which could be up to 4 people)
+ A space for Today’s Anniversaries (which could be up to 4 people)
+ A space for Today’s Visitor (which could be up to 2 people)
+ A space for a Picture of the Day
+ A space for Weather Forecast (perhaps a graphic)
+ A small "banner" section or strip for scrolling Notices / Alerts (perhaps at the bottom of the page?)

The deliverables for the layout need to include the HTML, applicable CSS, HTML code, etc. We need this to be relatively turnkey.

I have included in the contest package a hi-res JPG and AI for our Company Logo.

From a color pallet perspective:

Light Blue:
RGB - 21, 191,242
HEX - #15BFF2

Dark Blue:
RGB - 0, 70, 154
HEX - #00469A

Additionally, I have done a contest like this before (for another company I was at) and have included a screen shot of that final display.

PLEASE NOTE: IT DOES NOT HAVE TO LOOK EXACTLY LIKE THE ATTACHED SCREEN SHOT FROM THE PREVIOUS CONTEST. Including the screenshot was just to give you a general idea of some inspiration and objectives.

Feedback and questions are encouraged.

Target Market(s)

Our Employees

Industry/Entity Type

Digital

Number of Pages Required

1 page

Requirements
Must have
• + Our Logo
• + Our Company Name (Vorlan Aerotek)
• + Our "Tag Line" - "Progress Shaped By Practice, Quality Shaped By Dedication"
• + Date and Time
• + A space for Today’s Birthdays (which could be up to 4 people)
• + A space for Today’s Anniversaries (which could be up to 4 people)
• + A space for Today’s Visitor (which could be up to 2 people)
• + A space for a Picture of the Day
• + A space for Weather Forecast (perhaps a graphic)
• + A small "banner" section or strip for scrolling Notices / Alerts (perhaps at the bottom of the page?)

```html
<!DOCTYPE html>
<html lang="en">
<head>
<meta charset="utf-8">
<title>Vorlan Aerotek – Entrance Display</title>
<link rel="stylesheet" href="https://fonts.googleapis.com/css2?family=Source+Sans+3:wght@300;400;600;700&display=swap">
<style>
  :root {
    --bg-top: #fbfbfb;
    --bg-bottom: #e9e9e9;
    --brand-dark: #1f3a93;
    --brand-light: #15bff2;
    --ink: #4a4a4a;
    --white: #ffffff;
    --tile-picture: #4391d0;
    --tile-anniversary: #fbb83b;
    --tile-birthday: #e04a55;
    --tile-notice: #be520e;
    --tile-weather: #5ba321;
    --tile-visitors: #336791;
  }
  * { box-sizing: border-box; margin: 0; padding: 0; }
  html, body { width: 1200px; height: 675px; overflow: hidden; }
  body {
    font-family: "Source Sans 3", "Segoe UI", sans-serif;
    background: radial-gradient(ellipse at 50% 35%, var(--bg-top) 0%, var(--bg-top) 45%, var(--bg-bottom) 100%);
    position: relative;
    color: var(--white);
  }
  .masthead {
    position: absolute; left: 33px; right: 33px; top: 36px; height: 66px;
    display: flex; align-items: center;
  }
  .brand {
    display: flex; align-items: center; gap: 10px;
    color: var(--brand-dark); font-weight: 700; font-size: 27px; letter-spacing: 0.2px;
    padding-right: 16px; height: 62px;
  }
  .brand-mark { width: 14px; height: 14px; background: var(--brand-light); }
  .tagline {
    border-left: 2px solid var(--brand-light);
    padding-left: 18px; height: 62px;
    display: flex; flex-direction: column; justify-content: center;
    color: var(--brand-dark); font-size: 15px; line-height: 18px;
  }
  .tagline strong { font-weight: 600; }
  .datetime {
    margin-left: auto; text-align: right; color: var(--ink); font-weight: 300;
  }
  .datetime .day { font-size: 28px; line-height: 30px; }
  .datetime .stamp { font-size: 19px; line-height: 24px; }

  .board {
    position: absolute; left: 33px; top: 118px; width: 1134px; height: 504px;
    display: grid;
    grid-template-columns: repeat(3, 1fr);
    grid-template-rows: 206px 111px 179px;
    gap: 4px;
  }
  .tile {
    display: flex; flex-direction: column; align-items: center; justify-content: center;
    font-weight: 300; text-align: center;
  }
  .tile-picture { background: var(--tile-picture); grid-row: 1 / 4; grid-column: 1; padding-bottom: 20px; }
  .tile-anniversary { background: var(--tile-anniversary); grid-row: 1; grid-column: 2; }
  .tile-birthday { background: var(--tile-birthday); grid-row: 1; grid-column: 3; }
  .tile-notice { background: var(--tile-notice); grid-row: 2 / 4; grid-column: 2; }
  .tile-weather { background: var(--tile-weather); grid-row: 2; grid-column: 3; flex-direction: row; justify-content: flex-start; padding-left: 26px; }
  .tile-visitors { background: var(--tile-visitors); grid-row: 3; grid-column: 3; }

  .tile-title { font-size: 30px; line-height: 36px; }
  .tile-picture .tile-title { font-size: 33px; margin-top: 28px; }
  .tile-anniversary .tile-title, .tile-birthday .tile-title { margin-top: 14px; }
  .tile-visitors .tile-title { font-size: 32px; margin-top: 10px; }

  .notice-text { font-size: 20px; line-height: 24px; font-weight: 400; margin-top: 34px; }
  .weather-info { margin-left: 42px; text-align: center; }
  .weather-city { font-size: 16px; line-height: 20px; }
  .weather-reading { font-size: 25px; line-height: 30px; }
  .weather-reading sup { font-size: 11px; vertical-align: 11px; }
</style>
</head>
<body>
  <header class="masthead">
    <div class="brand"><span class="brand-mark"></span>Vorlan Aerotek</div>
    <div class="tagline">
      <span><strong>Progress</strong> shaped by <strong>practice</strong>,</span>
      <span><strong>Quality</strong> shaped by <strong>dedication</strong>.</span>
    </div>
    <div class="datetime">
      <div class="day">Saturday</div>
      <div class="stamp">Sep 6, 4:45am CDT</div>
    </div>
  </header>

  <main class="board">
    <section class="tile tile-picture">
      <svg width="160" height="140" viewBox="0 0 160 140" aria-hidden="true">
        <path d="M6 4 H140 V14 H16 V118 H6 Z" fill="#fff"/>
        <rect x="28" y="24" width="128" height="112" fill="none" stroke="#fff" stroke-width="8"/>
        <circle cx="56" cy="60" r="11" fill="#fff"/>
        <path d="M40 108 L78 78 L96 92 L128 54 L140 108 Z" fill="#fff"/>
      </svg>
      <h2 class="tile-title">Picture of the day</h2>
    </section>

    <section class="tile tile-anniversary">
      <svg width="70" height="80" viewBox="0 0 70 80" aria-hidden="true">
        <g fill="#fff">
          <circle cx="38" cy="12" r="8"/><circle cx="52" cy="18" r="8"/><circle cx="28" cy="22" r="8"/>
          <circle cx="46" cy="30" r="8"/><circle cx="58" cy="32" r="6"/><circle cx="36" cy="36" r="7"/>
          <path d="M30 42 L44 48 L14 78 L6 72 Z"/>
        </g>
      </svg>
      <h2 class="tile-title">Today’s Anniversaries</h2>
    </section>

    <section class="tile tile-birthday">
      <svg width="90" height="82" viewBox="0 0 90 82" aria-hidden="true">
        <g fill="#fff">
          <path d="M45 2 C50 8 49 13 45 13 C41 13 40 8 45 2 Z"/>
          <rect x="43" y="16" width="4" height="12"/>
          <rect x="6" y="30" width="78" height="14" rx="2"/>
          <rect x="6" y="48" width="78" height="10"/>
          <rect x="6" y="62" width="78" height="10"/>
          <rect x="0" y="75" width="90" height="6" rx="2"/>
        </g>
      </svg>
      <h2 class="tile-title">Today’s Birthdays</h2>
    </section>

    <section class="tile tile-notice">
      <svg width="74" height="66" viewBox="0 0 74 66" aria-hidden="true">
        <path d="M37 2 L72 64 H2 Z" fill="#fff" stroke="#fff" stroke-width="3" stroke-linejoin="round"/>
        <rect x="33" y="20" width="8" height="26" rx="3" fill="var(--tile-notice)"/>
        <circle cx="37" cy="54" r="4.5" fill="var(--tile-notice)"/>
      </svg>
      <p class="notice-text">Pay attention while walking,<br>your Chatterly status update can wait.</p>
    </section>

    <section class="tile tile-weather">
      <svg width="114" height="72" viewBox="0 0 114 72" aria-hidden="true">
        <path d="M22 66 C10 66 4 58 4 50 C4 40 12 33 22 33 C24 18 36 6 54 6 C70 6 82 16 86 30 C100 30 110 40 110 50 C110 60 102 66 92 66 Z"
              fill="none" stroke="#fff" stroke-width="7" stroke-linejoin="round"/>
      </svg>
      <div class="weather-info">
        <div class="weather-city">San Antonio</div>
        <div class="weather-reading">77<sup>°F</sup> Cloudy</div>
      </div>
    </section>

    <section class="tile tile-visitors">
      <svg width="56" height="68" viewBox="0 0 56 68" aria-hidden="true">
        <circle cx="28" cy="14" r="13" fill="#fff"/>
        <path d="M2 68 V40 C2 33 7 29 14 29 H42 C49 29 54 33 54 40 V68 Z" fill="#fff"/>
      </svg>
      <h2 class="tile-title">Today’s Visitors</h2>
    </section>
  </main>
</body>
</html>
```